Brolvane Co.,Ltd. need business card

Brolvane Company Limited is a facility management company. We provides a total solution services from administration, energy saving, security, safety, food catering to companies.

The logo should be in elegant style with innovative that suited to the upper market
Please see the logo image in the attached file. You can use this Red or Blue or Green checkerboard (color and font should be similar to logo) as the main part of business card (can be an entire of one side of business card) . In another side of card should contain contact details of personnel - here below demo information

Kanyarat Thoengsai
Chief Executive Officer

No.73, Soi 5, Ruam Wongsa Road
Nong Khaem, Bangkok,
10520, Thailand

Tel + 66841537296
Mobile + 66841537296
E-mail: Kanyarat.Thoengsai@brolvane-example.co.th

Target Market(s)

Factory, Hotel and Hospital

Industry/Entity Type

Business

Contact Information for Business Card

Kanyarat Thoengsai
Chief Executive Officer

Nong Khaem, Bangkok,
10520, Thailand

Tel + 66841537296
Mobile + 66841537296

We will change details with the winner designer

Font styles to use
Sans Serif

Requirements
Must have
• In style of red checkerboard and white color

```html
<!DOCTYPE html>
<html lang="en">
<head>
<meta charset="utf-8">
<title>Brolvane Co.,Ltd. – Business Card</title>
<link rel="stylesheet" href="https://fonts.googleapis.com/css2?family=Rasa:wght@300;400&display=swap">
<style>
  :root {
    --card-red: #8e191c;
    --ink-white: #ffffff;
    --name-dark: #2a2020;
    --title-rose: #c85a5c;
    --divider-rose: #c8625f;
  }
  html, body {
    margin: 0;
    padding: 0;
    overflow: hidden;
    background: var(--card-red);
  }
  .card {
    position: relative;
    width: 1200px;
    height: 695px;
    overflow: hidden;
    background: var(--card-red);
    font-family: "Rasa", Georgia, serif;
    color: var(--ink-white);
  }
  .company-name {
    position: absolute;
    left: 48px;
    top: 58px;
    margin: 0;
    font-size: 64px;
    font-weight: 300;
    line-height: 1;
    white-space: nowrap;
    color: var(--ink-white);
  }
  .person {
    position: absolute;
    right: 159px;
    top: 258px;
    text-align: right;
  }
  .person-name {
    margin: 0;
    font-size: 65px;
    font-weight: 300;
    line-height: 1;
    white-space: nowrap;
    color: var(--name-dark);
  }
  .person-title {
    margin: 2px 0 0;
    font-size: 48px;
    font-weight: 300;
    line-height: 1;
    white-space: nowrap;
    color: var(--title-rose);
  }
  .divider {
    position: absolute;
    left: 501px;
    top: 430px;
    width: 2px;
    height: 230px;
    background: var(--divider-rose);
  }
  .address {
    position: absolute;
    right: 729px;
    top: 446px;
    margin: 0;
    text-align: right;
    font-style: normal;
    font-size: 42px;
    font-weight: 300;
    line-height: 48px;
    white-space: nowrap;
  }
  .contacts {
    position: absolute;
    left: 527px;
    top: 467px;
    margin: 0;
    padding: 0;
    list-style: none;
  }
  .contact {
    display: flex;
    align-items: center;
    height: 44px;
    margin-bottom: 16px;
    font-size: 41px;
    font-weight: 300;
    white-space: nowrap;
  }
  .contact-icon {
    width: 44px;
    height: 44px;
    margin-right: 26px;
    flex: none;
  }
  .contact-email { font-size: 31px; }
</style>
</head>
<body>
<main class="card">
  <h1 class="company-name">Brolvane Co.,Ltd.</h1>

  <section class="person">
    <h2 class="person-name">KANYARAT THOENGSAI</h2>
    <p class="person-title">Chief Executive Officer</p>
  </section>

  <address class="address">
    No.73, Soi 5<br>
    Ruam Wongsa Road<br>
    Nong Khaem, Bangkok,<br>
    10520, Thailand
  </address>

  <div class="divider"></div>

  <ul class="contacts">
    <li class="contact">
      <svg class="contact-icon" viewBox="0 0 44 44" aria-hidden="true">
        <circle cx="22" cy="22" r="22" fill="#fff"/>
        <path d="M15 12c1-1 2.5-1 3.3 0l2.2 3c.6.9.4 2-.4 2.7l-1.3 1c.9 2.4 2.8 4.3 5.2 5.4l1-1.3c.7-.8 1.9-1 2.8-.3l3 2.1c1 .8 1 2.3 0 3.2l-1.6 1.5c-1.2 1.1-3 1.3-4.5.6-5-2.4-9-6.4-11.2-11.5-.6-1.5-.3-3.2.8-4.3z" fill="#8e191c"/>
      </svg>
      <span>+ 66841537296</span>
    </li>
    <li class="contact">
      <svg class="contact-icon" viewBox="0 0 44 44" aria-hidden="true">
        <circle cx="22" cy="22" r="22" fill="#fff"/>
        <rect x="15" y="9" width="14" height="26" rx="2.5" fill="#8e191c"/>
        <rect x="17" y="12.5" width="10" height="17" fill="#fff"/>
        <circle cx="22" cy="32.2" r="1.3" fill="#fff"/>
      </svg>
      <span>+ 66841537296</span>
    </li>
    <li class="contact contact-email">
      <svg class="contact-icon" viewBox="0 0 44 44" aria-hidden="true">
        <circle cx="22" cy="22" r="22" fill="#fff"/>
        <rect x="11" y="14" width="22" height="16" fill="#8e191c"/>
        <path d="M11.5 14.5 22 23.5l10.5-9M11.5 29.5l8-7.5M32.5 29.5l-8-7.5" fill="none" stroke="#fff" stroke-width="1.5"/>
      </svg>
      <span>Kanyarat.Thoengsai@brolvane-example.co.th</span>
    </li>
  </ul>
</main>
</body>
</html>
```